依頼詳細
(例)毎年忘年会・新年会チラシをうちます。その広告デザインをお願い致します。今年は新企画として女子会プランを紙面の半分のスペースに入れたいと思います。明るく楽しく見やすい和のデザインをお願いします。
記載項目
(例)入る原稿(文字、写真)はイラストレーターCS2にて添付します。裏面は昨年から流用しますので表面には住所や地図は入りません。タイトルをいじったりキャッチコピーを入れて下さってかまいません。
希望イメージ
シンプル 複雑
単色 カラフル
暗い 明るい
日常 高級
遊び心 厳粛
未来的 伝統的
女性的 男性的
希望する色
(例)赤、黒(特にこだわりません)
納品ファイル
• 高解像度JPG (.jpg)
• イラストレーター形式 (.ai)
補足説明
■ 選んだ理由

明るく楽しげな雰囲気がとてもよかったです。女子会のタイトルの工夫もいい感じです。

■ 提案者全員のお礼・コメント

多くの方に提案して頂きありがとうございました。1つ選ぶのは心苦しいのですが選んだ納得感が気に入っています。またお願いするときにはよろしくお願いします。

```html
<!DOCTYPE html>
<html lang="ja">
<head>
<meta charset="utf-8">
<title>忘年会・新年会 ご案内</title>
<link rel="stylesheet" href="https://fonts.googleapis.com/css2?family=Yuji+Syuku&family=Zen+Old+Mincho:wght@700;900&family=Noto+Sans+JP:wght@400;700;900&display=swap">
<style>
:root{
  --paper:#f4ecd8;
  --paper-dark:#e9dcbd;
  --blue:#1e4f9c;
  --red:#d9262c;
  --orange:#ec6b1e;
  --green:#3c8a3a;
  --brown:#5a3a22;
  --gold:#c79a3a;
  --pink:#f6c8d6;
  --pink-deep:#e7548a;
  --ink:#2a1e14;
  --white:#fff;
}
*{margin:0;padding:0;box-sizing:border-box}
html,body{width:847px;height:1200px;overflow:hidden}
body{font-family:"Noto Sans JP",sans-serif;color:var(--ink);background:var(--paper)}
.flyer{position:relative;width:847px;height:1200px;background:linear-gradient(180deg,var(--paper) 0%,var(--paper-dark) 40%);border:8px solid #b8945a;overflow:hidden}
.pattern{position:absolute;left:0;top:0;width:100%;height:480px;background:radial-gradient(circle at 20% 30%,#efe0bf 0 60px,transparent 61px),radial-gradient(circle at 70% 15%,#efe0bf 0 70px,transparent 71px),radial-gradient(circle at 40% 80%,#efe0bf 0 50px,transparent 51px)}
.catch{position:absolute;left:22px;top:14px;font-family:"Yuji Syuku",serif;font-size:24px;line-height:1.35;color:var(--green)}
.catch span{color:var(--red)}
.title{position:absolute;left:18px;font-family:"Zen Old Mincho",serif;font-weight:900;font-size:106px;letter-spacing:4px;line-height:1;-webkit-text-stroke:3px var(--white);paint-order:stroke fill}
.title.year-end{top:78px;color:var(--blue)}
.title.new-year{top:184px;left:52px;color:var(--red)}
.brand{position:absolute;left:330px;top:292px;display:flex;align-items:center;gap:8px;font-family:"Zen Old Mincho",serif;font-weight:900;font-size:36px;line-height:1;color:var(--ink)}
.brand i{width:12px;height:12px;background:var(--red);display:block}

.course-panel{position:absolute;left:484px;top:18px;width:345px;height:392px;background:var(--white);border:3px solid var(--gold);border-radius:6px;padding:8px 14px}
.course-panel h2{font-size:18px;font-weight:700;line-height:1.3;color:var(--brown)}
.course-panel .from{font-size:28px;font-weight:900;line-height:1.3;color:var(--red);margin-bottom:2px}
.course-panel .from small{font-size:15px}
.course{border-top:1px dashed var(--gold);padding:4px 0 3px;display:grid;grid-template-columns:1fr auto;align-items:end}
.course b{font-family:"Zen Old Mincho",serif;font-size:22px;line-height:1.2;color:var(--red)}
.course b small{font-size:10px;color:var(--ink)}
.course .price{font-size:22px;font-weight:900;line-height:1.15;color:var(--red);text-align:right}
.course .price small{display:block;font-size:9px;line-height:1.2;color:var(--ink);font-weight:400}
.course p{grid-column:1/3;font-size:9.5px;line-height:1.3;color:#5b4a3a}

.band{position:absolute;left:20px;width:455px;height:60px;border-radius:4px;display:flex;align-items:center;padding:0 12px;gap:12px}
.band.drink{top:342px;background:var(--white);border:3px solid var(--orange)}
.band.nabe{top:414px;background:var(--orange);color:var(--white)}
.band .name{font-family:"Zen Old Mincho",serif;font-weight:900;font-size:26px;color:var(--red)}
.band.nabe .name{color:var(--white)}
.band .amount{font-size:30px;font-weight:900;color:var(--red)}
.band.nabe .amount{color:var(--white)}
.band .amount small{font-size:14px}
.band .tag{background:var(--red);color:var(--white);font-size:11px;font-weight:700;padding:4px 5px;writing-mode:vertical-rl}
.band .note{font-size:10px;line-height:1.35}
.nabe-photo{margin-left:auto;width:120px;height:50px;border-radius:4px;background:linear-gradient(135deg,#c9873f,#7a4a22)}

.discount{position:absolute;left:484px;top:418px;width:345px;height:56px;background:var(--white);border:2px solid var(--red);display:flex;align-items:center;gap:10px;padding:0 12px}
.discount strong{font-size:24px;font-weight:900;color:var(--red)}
.discount span{font-size:11px;line-height:1.35}

.girls{position:absolute;left:12px;top:490px;width:807px;height:688px;background:linear-gradient(180deg,#fbdde6,var(--pink));border-radius:14px;border:3px solid var(--pink-deep)}
.girls .lead{position:absolute;left:40px;top:14px;font-size:17px;font-weight:700;color:var(--pink-deep)}
.girls h2{position:absolute;left:40px;top:40px;font-family:"Zen Old Mincho",serif;font-weight:900;font-size:58px;color:var(--white);-webkit-text-stroke:2px var(--pink-deep);paint-order:stroke fill}
.girls .sushi-title{position:absolute;left:480px;top:60px;font-family:"Zen Old Mincho",serif;font-weight:900;font-size:28px;color:var(--pink-deep)}
.photo{position:absolute;border-radius:12px}
.photo.zen{left:150px;top:130px;width:300px;height:270px;background:radial-gradient(circle,#e8b26a,#8a4a2a)}
.photo.sushi{left:480px;top:110px;width:310px;height:300px;background:radial-gradient(circle,#f3e6d3,#c44a3a)}
.plan{position:absolute;color:var(--pink-deep)}
.plan .pname{font-family:"Zen Old Mincho",serif;font-weight:900;font-size:30px;line-height:1.25}
.plan .pprice{font-size:44px;font-weight:900;line-height:1.2;color:var(--red)}
.plan .pprice small{font-size:20px}
.plan .tax{font-size:14px;color:var(--ink)}
.plan .drinks{font-size:16px;color:var(--ink)}
.plan.zen{left:30px;top:140px;width:120px}
.plan.zen .price-block{position:absolute;left:0;top:285px;width:300px}
.plan.sushi{left:610px;top:430px;text-align:right;width:180px}
.sushi-menu{position:absolute;left:480px;top:440px;width:130px;font-size:13px;line-height:1.55;color:var(--ink)}
</style>
</head>
<body>
<div class="flyer">
  <div class="pattern" role="img" aria-label="扇と和柄の地模様"></div>
  <div class="catch">いく年、<br><span>くる年</span>の御予約に</div>
  <div class="title year-end">忘年会</div>
  <div class="title new-year">新年会</div>
  <div class="brand"><i></i>大和亭</div>

  <section class="course-panel">
    <h2>法要後のお食事<br>宴会用会席料理</h2>
    <div class="from">3,500<small>円より</small></div>
    <div class="course"><b>彩 <small>いろどり</small></b><div class="price">3,500円<small>(税込3,675円)</small></div><p>先付・お造り・焼物・煮物・揚物・茶碗蒸し・御飯・甘味</p></div>
    <div class="course"><b>雅 <small>みやび</small></b><div class="price">4,000円<small>(税込4,200円)</small></div><p>先付・お造り・焼物・煮物・天ぷら・寿司・吸物・甘味</p></div>
    <div class="course"><b>曙 <small>あけぼの</small></b><div class="price">5,000円<small>(税込5,250円)</small></div><p>前菜・上造り・焼物・煮物・天ぷら・上寿司・吸物・甘味</p></div>
    <div class="course"><b>葵 <small>あおい</small></b><div class="price">7,000円<small>(税込7,350円)</small></div><p>前菜・特上造り・焼物・煮物・天ぷら・特上寿司・甘味</p></div>
  </section>

  <div class="band drink"><span class="name">得々飲み放題</span><span class="tag">要予約</span><span class="amount">5,000<small>円より</small></span><span class="note">2時間制<br>10名様より</span></div>
  <div class="band nabe"><span class="name">寄せ鍋</span><span class="amount">3,500<small>円より</small></span><div class="nabe-photo" role="img" aria-label="寄せ鍋の写真"></div></div>

  <div class="discount"><strong>5%OFF</strong><span>お会計時にこの紙をご持参の<br>お客様に限り5%割引いたします</span></div>

  <section class="girls">
    <div class="lead">女性のお客様にお得なプラン</div>
    <h2>女子会セット</h2>
    <div class="sushi-title">女子会上寿司コース</div>
    <div class="photo zen" role="img" aria-label="女子会新膳コースの料理写真"></div>
    <div class="photo sushi" role="img" aria-label="上寿司と前菜の料理写真"></div>
    <div class="plan zen">
      <div class="pname">女子会<br>新膳<br>コース</div>
      <div class="price-block"><div class="pprice">2,500<small>円</small></div><div class="tax">(税込2,625円)</div><div class="drinks">ソフトドリンク付き</div></div>
    </div>
    <div class="sushi-menu">先付<br>茶碗蒸し<br>デザート<br>ソフトドリンク付き</div>
    <div class="plan sushi"><div class="pprice">2,500<small>円</small></div><div class="tax">(税込2,625円)</div></div>
  </section>
</div>
</body>
</html>
```